Website Landing Page for Brightfall Systems

Create a custom designed website landing page for our business. Looking for a professional upscale design that incorporates our logo and logo colors into the theme. I want a standard fixed frame website, not a constant scrolling format that seems to be the trend. To start with I'm looking for more of the graphic design part, maybe a concept or theme, I don't expect to see a finished project. Not interested in generic templates or layouts.

The name of our company is Brightfall Systems and I've attached our logo below. I'd like to have the web page have the same look and feel of our logo, as well as the colors. Our company, Brightfall Systems does system design, installation, and programming, of residential and commercial Audio/Video and Automation systems. We do home theaters, lighting and building automation, video conferencing systems, security camera installations, conference rooms, projectors, distributed audio systems, and similar Technology projects. This will be a professional services/informational website. We will not sell products on this website. This website will be used to advertise our company and communicate our services to prospective customers. Having a well designed, professional and clean website is one way we want to distinguish our company from the competition.

Here are some examples of what I consider a professional well designed website
http://www.qorlamstudio.com/Work/

Last year we had our tradlo store designed (with PixelMarket) and I'm really happy with the way it turned out. You can see it at www.HolvenGearDepot.com I consider this to be a great design and looking for the same level of quality with this new website. However, do not copy or use any part of this design in this new project. This tradlo store is completely separate from our other company Brightfall Systems. I only mention this tradlo store an an example of good work.

Reason: Still going through designs.

Reason: Still working on project and have not had time to review all designs and request revisions.

Reason: Sill going through designs and requesting revisions

Reason: still going through all the submissions we received.

Target Market(s)

People interested in Audio/Video, home theaters, home automation. We do sales, system design, and programming. We typically work on larger projects with both residential and commercial customers.

Industry/Entity Type

Business

Number of Pages Required

1 page

Requirements
Must have
• Great design elements. Please use a white background. I think white goes well with our logo colors.

```html
<!DOCTYPE html>
<html lang="en">
<head>
<meta charset="utf-8">
<title>Brightfall Systems</title>
<link href="https://fonts.googleapis.com/css2?family=Roboto:wght@400;500;700&family=Lato:wght@400;700&family=Noto+Serif:ital@1&display=swap" rel="stylesheet">
<style>
:root{
  --blue:#3a80c8;
  --blue-dark:#2f6fb4;
  --cyan:#2fbde8;
  --green:#8cc63f;
  --ink:#222;
  --text:#555;
  --muted:#999;
  --line:#e3e3e3;
  --panel:#f1f2f4;
  --white:#fff;
}
*{margin:0;padding:0;box-sizing:border-box}
html,body{width:751px;height:1200px;overflow:hidden;background:var(--white)}
body{position:relative;font-family:'Lato',sans-serif;color:var(--text)}
.abs{position:absolute}
h2,h3,h4,.nav,.btn{font-family:'Roboto',sans-serif}

/* header */
.site-header{left:0;top:0;width:751px;height:61px;background:var(--white)}
.brand{left:70px;top:9px;display:flex;align-items:center;gap:8px}
.brand-mark{width:42px;height:42px;border-radius:50%;border:4px solid var(--cyan)}
.brand-name{font-family:'Roboto',sans-serif;font-weight:700;font-size:13px;line-height:14px;color:var(--blue);letter-spacing:.5px}
.top-phone,.top-enquire{top:2px;height:22px;color:var(--white);font-size:8.5px;font-weight:700;display:flex;align-items:center;justify-content:center;gap:5px;font-family:'Roboto',sans-serif;transform:skewX(-15deg)}
.top-phone span,.top-enquire span{transform:skewX(15deg);display:flex;align-items:center;gap:5px}
.top-phone{left:498px;width:90px;background:var(--cyan)}
.top-enquire{left:590px;width:88px;background:var(--green)}
.nav{left:336px;top:42px;display:flex;gap:15px;font-size:8.5px;font-weight:500;color:#333;letter-spacing:.2px}

/* hero */
.hero{left:0;top:61px;width:751px;height:321px;background:linear-gradient(180deg,#d9d2c6 0%,#a89480 45%,#6b5442 72%,#cfc6b8 100%)}

/* services */
.service{top:382px;width:95px;height:70px;background:var(--white);border:1px solid var(--line);border-top:none;text-align:center}
.service-ring{position:absolute;left:17px;top:-30px;width:60px;height:60px;border-radius:50%;background:var(--white);border:3px solid var(--blue);display:flex;align-items:center;justify-content:center}
.service-ring i{width:46px;height:46px;border-radius:50%;background:radial-gradient(circle,#8cc63f 0 30%,#2fbde8 32%)}
.service-label{position:absolute;left:0;right:0;top:42px;font-family:'Roboto',sans-serif;font-size:7px;font-weight:500;color:#333;line-height:9.5px}

/* welcome */
.welcome{left:0;top:452px;width:751px;height:259px;background:linear-gradient(180deg,#f4f4f5,#e9eaec)}
.welcome h2{left:70px;top:46px;font-size:13px;font-weight:500;color:var(--ink)}
.welcome p{left:70px;width:390px;font-size:7.6px;line-height:12.8px;color:#666}
.read-more{left:70px;top:204px;font-size:7px;font-weight:700;color:var(--blue);font-family:'Roboto',sans-serif}
.reviews{left:488px;top:485px;width:263px;height:226px;background:var(--blue)}
.reviews-corner{left:488px;top:485px;width:0;height:0;border-top:16px solid var(--cyan);border-right:16px solid transparent}
.reviews h3{left:17px;top:29px;font-size:12px;font-weight:500;color:var(--white)}
.quote-mark{left:17px;top:55px;font-family:'Noto Serif',serif;font-size:20px;color:var(--cyan);line-height:1}
.quote{left:37px;top:57px;width:160px;font-family:'Noto Serif',serif;font-style:italic;font-size:7.6px;line-height:12.8px;color:var(--white)}
.avatar{left:37px;top:144px;width:34px;height:34px;border-radius:50%;background:#dde6ef;border:2px solid var(--white)}
.reviewer{left:78px;top:148px;color:var(--white);font-family:'Roboto',sans-serif}
.reviewer b{display:block;font-size:9px;font-weight:500}
.reviewer small{font-size:7.5px;color:#dce8f5}
.dots{left:112px;top:190px;display:flex;gap:3px}
.dots i{width:4px;height:4px;border-radius:50%;background:#8db6e2}
.dots i:first-child{background:var(--cyan)}

/* blog & projects */
.section-title{top:741px;font-size:12.5px;font-weight:500;color:var(--ink)}
.post{top:772px;width:192px}
.post h4{font-size:8.8px;font-weight:500;color:var(--ink)}
.post .meta{margin-top:5px;font-size:7px;color:var(--muted);padding-bottom:6px;border-bottom:1px solid var(--line)}
.post .thumb{position:absolute;left:0;top:43px;width:73px;height:58px}
.post p{position:absolute;left:81px;top:47px;width:110px;font-size:7.3px;line-height:11.8px;color:#666}
.post .btn{position:absolute;left:80px;top:86px;width:52px;height:15px;background:var(--cyan);color:var(--white);font-size:6.5px;font-weight:700;display:flex;align-items:center;justify-content:center}
.project{left:488px;top:774px;width:194px;height:108px;background:linear-gradient(160deg,#cbb48f,#8b7258 60%,#c9c1b2);border:1px solid #ccc}
.project-bar{left:0;bottom:0;width:100%;height:22px;background:rgba(20,20,20,.82);display:flex;align-items:center;justify-content:space-between;padding:0 6px 0 7px;color:var(--white);font-family:'Roboto',sans-serif;font-size:7.5px;font-weight:700}
.project-bar i{width:12px;height:12px;border-radius:50%;background:var(--green);display:flex;align-items:center;justify-content:center}

/* call to action */
.cta{left:0;top:930px;width:751px;height:80px;background:var(--cyan)}
.cta-left{left:0;top:0;width:751px;height:80px}
.cta h2{left:69px;top:19px;font-size:12.5px;font-weight:500;color:var(--white)}
.cta p{left:69px;top:40px;width:300px;font-size:7.3px;line-height:11.8px;color:var(--white)}
.support-photo{left:372px;top:912px;width:68px;height:98px;background:linear-gradient(180deg,#3aa6c4,#1f9aa0)}
.cta-btn{top:26px;height:29px;display:flex;align-items:center;justify-content:center;font-size:9px;font-weight:500;font-family:'Roboto',sans-serif}
.cta-btn.outline{left:451px;width:112px;border:2px solid var(--white);color:var(--white)}
.cta-btn.solid{left:569px;width:113px;background:var(--white);color:var(--blue)}

/* footer */
.site-footer{left:0;top:1010px;width:751px;height:190px;background:#f4f4f4}
.foot-col{top:24px;font-size:7.3px;color:#666;line-height:13.8px}
.foot-col h4{font-size:7px;font-weight:700;color:#333;margin-bottom:4px;line-height:10px}
.socials{display:flex;gap:4px;margin-top:10px}
.socials i{width:17px;height:17px;border-radius:50%;border:1.5px solid #555}
.foot-brand{left:575px;top:24px;width:110px;text-align:center}
.foot-brand .mark{width:62px;height:62px;border-radius:50%;border:6px solid var(--cyan);margin:0 auto 6px}
.foot-brand b{font-family:'Roboto',sans-serif;font-weight:700;font-size:15px;line-height:17px;color:var(--blue);letter-spacing:.5px}
.copyright{left:0;top:164px;width:751px;text-align:center;font-size:7.3px;color:#555}
</style>
</head>
<body>

<header class="site-header abs">
  <div class="brand abs"><div class="brand-mark"></div><div class="brand-name">BRIGHTFALL<br>SYSTEMS</div></div>
  <div class="top-phone abs"><span>
    <svg width="7" height="9" viewBox="0 0 7 9"><rect x="0.5" y="0.5" width="6" height="8" rx="1" fill="none" stroke="#fff"/><rect x="2" y="6.5" width="3" height="1" fill="#fff"/></svg>
    1800 555 0142</span></div>
  <div class="top-enquire abs"><span>
    <svg width="8" height="8" viewBox="0 0 8 8"><path d="M1 7l1-3 4-4 2 2-4 4z" fill="#fff"/></svg>
    ENQUIRE NOW</span></div>
  <nav class="nav abs"><span>HOME</span><span>COMPANY</span><span>SERVICES</span><span>PRODUCTS</span><span>SOLUTIONS</span><span>BLOG</span><span>CONTACT</span></nav>
</header>

<div class="hero abs" role="img" aria-label="Living room with a wall-mounted screen showing a waterfall, media cabinet and sofa"></div>

<section class="services">
  <div class="service abs" style="left:70px"><div class="service-ring"><i role="img" aria-label="Home theater icon"></i></div><div class="service-label">HOME THEATERS</div></div>
  <div class="service abs" style="left:173px"><div class="service-ring"><i role="img" aria-label="Lighting icon"></i></div><div class="service-label">LIGHTING &amp; BUILDING<br>AUTOMATION</div></div>
  <div class="service abs" style="left:276px"><div class="service-ring"><i role="img" aria-label="Video conferencing icon"></i></div><div class="service-label">VIDEO CONFERENCING<br>SYSTEMS</div></div>
  <div class="service abs" style="left:379px"><div class="service-ring"><i role="img" aria-label="Security camera icon"></i></div><div class="service-label">SECURITY CAMERA<br>INSTALLATIONS</div></div>
  <div class="service abs" style="left:483px"><div class="service-ring"><i role="img" aria-label="Distributed audio icon"></i></div><div class="service-label">DISTRIBUTED<br>AUDIO SYSTEMS</div></div>
  <div class="service abs" style="left:586px"><div class="service-ring"><i role="img" aria-label="Projector icon"></i></div><div class="service-label">PROJECTORS</div></div>
</section>

<section class="welcome abs" role="img" aria-label="Faint city skyline backdrop">
  <h2 class="abs">Welcome to Brightfall Systems</h2>
  <p class="abs" style="top:76px">This is Photoshop's version &nbsp;of Lorem Ipsum. Proin gravida nibh vel velit auctor aliquet. Aenean sollicitudin, lorem quis bibendum auctor, nisi elit consequat ipsum, nec sagittis sem nibh id elit. Duis sed odio sit amet nibh vulputate cursus a sit amet mauris. Morbi accumsan ipsum velit. Nam nec tellus a odio tincidunt auctor a ornare odio. Sed non &nbsp;mauris vitae erat consequat auctor eu in elit. Class aptent taciti sociosqu ad litora torquent per conubia nostra, per inceptos himenaeos.</p>
  <p class="abs" style="top:154px">Mauris in erat justo. Nullam ac urna eu felis dapibus condimentum sit amet a augue. Sed non neque elit. Sed ut imperdiet nisi. Proin condimentum fermentum nunc. Etiam pharetra, velit mauris egestas quam, ut aliquam massa nisl quis neque. Suspendisse in orci enim.</p>
  <div class="read-more abs">READ MORE &#9656;</div>
</section>

<aside class="reviews abs">
  <h3 class="abs">Customer Reviews</h3>
  <div class="quote-mark abs">&ldquo;</div>
  <p class="quote abs">Lorem Ipsum proin gravida nibh vel velit auctor aliquet. Aenean sollicitudin, lorem quis bibendum auctor, nisi elit consequat ipsum, nec sagittis sem nibh id elit. Duis sed odio sit amet nibh vulputate cursus a sit amet mauris.</p>
  <div class="avatar abs" role="img" aria-label="Customer portrait"></div>
  <div class="reviewer abs"><b>Daniel Morrow</b><small>Lorem ipsum dolor</small></div>
  <div class="dots abs"><i></i><i></i><i></i><i></i><i></i></div>
</aside>
<div class="reviews-corner abs"></div>

<h2 class="section-title abs" style="left:69px">From the Blog</h2>
<article class="post abs" style="left:70px">
  <h4>Awesome lorem ipsum dolor sitting amet</h4>
  <div class="meta">&#9633; 03 March 2016 &nbsp;&nbsp; &#9675; 20 Comments</div>
  <div class="thumb" role="img" aria-label="Grand hotel lobby" style="background:linear-gradient(160deg,#c9a063,#6b4a2a)"></div>
  <p>Lorem ipsum dolor sit amet, consectetuer praesent well as luptatum zzril delenit.</p>
  <div class="btn">READ MORE</div>
</article>
<article class="post abs" style="left:279px">
  <h4>Awesome lorem ipsum dolor sitting amet</h4>
  <div class="meta">&#9633; 03 March 2016 &nbsp;&nbsp; &#9675; 20 Comments</div>
  <div class="thumb" role="img" aria-label="Living room with arched windows" style="background:linear-gradient(160deg,#d7c4a0,#8a5a3c)"></div>
  <p>Lorem ipsum dolor sit amet, consectetuer praesent well as luptatum zzril delenit.</p>
  <div class="btn">READ MORE</div>
</article>

<h2 class="section-title abs" style="left:487px">Recent Project Works</h2>
<div class="project abs" role="img" aria-label="Furnished lounge interior project">
  <div class="project-bar abs">AWESOME PROJECT<i><svg width="6" height="6" viewBox="0 0 6 6"><path d="M2 1l2 2-2 2" stroke="#fff" stroke-width="1.2" fill="none"/></svg></i></div>
</div>

<section class="cta abs">
  <svg class="cta-left abs" viewBox="0 0 751 80"><polygon points="0,0 344,0 376,80 0,80" fill="#3a80c8"/></svg>
  <h2 class="abs">How Can We help you?</h2>
  <p class="abs">We ready to help you. Give us a call or fill out this form to request service or ask a question about equipment. We look forward to visiting with you!</p>
  <div class="cta-btn outline abs">Contact Us Today!</div>
  <div class="cta-btn solid abs">Sign Up Newsletter</div>
</section>
<div class="support-photo abs" role="img" aria-label="Photo of a support agent wearing a headset"></div>

<footer class="site-footer abs">
  <div class="foot-col abs" style="left:69px">
    <h4>BRIGHTFALL SYSTEMS</h4>
    228, Lorem ipsum dolor sit,<br>dosos amet dill - 845848<br><br>
    T: 1800 555 0178<br>E: info@brightfallsystems.com<br>www.brightfallsystems.com
    <div class="socials"><i></i><i></i><i></i><i></i><i></i></div>
  </div>
  <div class="foot-col abs" style="left:270px">
    <h4>OUR SERVICES</h4>
    Home Theaters<br>Lighting and Building Automation<br>Video Conferencing Systems<br>Security Camera Installations<br>Conference Rooms<br>Projectors<br>Distributed Audio Systems
  </div>
  <div class="foot-col abs" style="left:463px">
    <h4>QUICK LINKS</h4>
    Home<br>Company<br>Services<br>Products<br>Solutions<br>Blog<br>Contact
  </div>
  <div class="foot-brand abs"><div class="mark"></div><b>BRIGHTFALL<br>SYSTEMS</b></div>
  <div class="copyright abs">&copy; 2017 Brightfall Systems.com. All Rights Reserved</div>
</footer>

</body>
</html>
```